Event Website Design

We need a new website design for an events driven website. The domain for this site is http://brackmoorhalls.co.uk. The site is up and running but needs a new fresh, modern look.
I've attached a Balamiq Mockup for the layout of the home page. Also attached is a png of the logo.
Key colours for the site are 0f7e6a, 35bde, d57835 & 373737.
Font to use is Proxima Nova
Width of the site should be 1200px
The design should be contemporary with minimal clutter.
Websites to references are…
http://vantora.london/
http://www.thekrd.co.uk/
These are just guidelines, please feel free to use you own creative judgment.
The selected design file needs to be supplied as an editable PSD.
Updates
Reason: I've submitted 5 designs to the client, who will select the one they want. I will then choose that design. So please be patient as I'm waiting for a decision from my client.
Industry/Entity Type
Events
Number of Pages Required
1 page
Look and feel
Each slider illustrates characteristics of the customer's brand and the style your logo design should communicate.

```html
<!DOCTYPE html>
<html lang="en">
<head>
<meta charset="utf-8">
<title>Brackmoor Halls – Home</title>
<link rel="stylesheet" href="https://fonts.googleapis.com/css2?family=Montserrat:wght@400;500;600;700&display=swap">
<style>
:root{
  --green:#0f7e6a;
  --blue:#135bde;
  --orange:#d57835;
  --dark:#373737;
  --ink:#2b2b2b;
  --grey-text:#666;
  --light-bg:#f2f2f2;
  --white:#fff;
}
*{box-sizing:border-box;margin:0;padding:0}
html,body{width:1200px;height:2932px;overflow:hidden;background:var(--white);font-family:"Montserrat",sans-serif;color:var(--ink)}
.page{position:relative;width:1200px;height:2932px}

/* header */
.site-header{position:absolute;left:0;top:0;width:1200px;height:160px;background:var(--dark);color:var(--white)}
.brand{position:absolute;left:147px;top:54px;display:flex;align-items:center;gap:12px;font-weight:700;font-size:28px;letter-spacing:1px}
.brand-dot{width:16px;height:16px;background:var(--green)}
.tagline{position:absolute;left:98px;top:128px;font-size:12px;color:#cfcfcf}
.utility{position:absolute;right:133px;top:16px;display:flex;gap:30px;font-size:11px;color:#e6e6e6}
.utility span{display:flex;align-items:center;gap:7px}
.utility i{display:inline-block;width:10px;height:10px;background:#e6e6e6;border-radius:2px}
.box-office{position:absolute;left:577px;top:62px;display:flex;align-items:center;gap:22px}
.phone-icon{width:44px;height:44px;border:1px solid #888;display:flex;align-items:center;justify-content:center}
.box-office small{display:block;font-size:10px;font-weight:600}
.box-office strong{display:block;font-size:22px;font-weight:600;margin-top:2px}
.search{position:absolute;left:907px;top:66px;width:160px;height:38px;border:1px solid #777;display:flex;align-items:center;gap:10px;padding-left:14px;font-size:9px;color:#bbb}
.follow{position:absolute;left:915px;top:124px;display:flex;align-items:center;gap:8px;font-size:10px}
.follow .dot{width:20px;height:20px;border-radius:50%}

/* nav */
.main-nav{position:absolute;left:0;top:160px;width:1200px;height:43px;background:var(--green);display:flex;justify-content:space-around;align-items:center;padding:0 100px 0 105px;font-size:12px;color:var(--white);font-weight:500}

/* hero */
.hero{position:absolute;left:0;top:203px;width:1200px;height:487px;background:linear-gradient(180deg,#6b4a32 0%,#8a5d38 35%,#5d3a22 70%,#3b2416 100%)}
.hero-copy{position:absolute;left:0;top:84px;width:1200px;text-align:center;color:var(--white)}
.hero-copy h2{font-size:20px;font-weight:600;letter-spacing:1px}
.hero-copy h1{font-size:56px;font-weight:700;letter-spacing:1px;margin-top:2px;line-height:1.1}
.hero-copy .date{font-size:15px;font-weight:500;margin-top:12px}
.hero-copy p{font-size:17px;font-weight:600;width:560px;margin:30px auto 0;line-height:27px}
.hero-btn{position:absolute;top:319px;height:56px;color:var(--white);font-size:19px;font-weight:500;display:flex;align-items:center;justify-content:center;gap:14px}
.hero-btn.more{left:430px;width:160px;background:var(--blue)}
.hero-btn.book{left:626px;width:162px;background:var(--orange)}
.dots{position:absolute;top:433px;left:0;width:1200px;display:flex;justify-content:center;gap:28px}
.dots span{width:8px;height:8px;border-radius:50%;background:var(--white)}
.dots span.on{background:none;border:2px solid var(--white);width:11px;height:11px;margin-top:-1px}

/* event carousel */
.event-card{position:absolute;top:743px;width:229px;height:324px;background:var(--white);box-shadow:0 1px 4px rgba(0,0,0,.15)}
.event-card .photo{height:164px}
.event-card h3{font-size:17px;font-weight:500;margin:22px 0 0 24px}
.event-card .when{margin:14px 0 0 24px;width:167px;height:33px;border:1.5px solid var(--green);font-size:11px;color:var(--grey-text);display:flex;align-items:center;justify-content:center}
.mini-btns{display:flex;gap:14px;margin:21px 0 0 24px}
.btn-s{height:28px;color:var(--white);font-size:9px;font-weight:600;display:flex;align-items:center;justify-content:center;gap:6px}
.btn-s.blue{background:var(--blue);width:72px}
.btn-s.orange{background:var(--orange);width:80px}
.btn-s.green{background:var(--green);width:72px}
.arrow{position:absolute;top:887px;width:44px;height:44px;border-radius:50%;border:1px solid #ccc;background:var(--white);display:flex;align-items:center;justify-content:center;box-shadow:0 1px 3px rgba(0,0,0,.12)}

/* news */
.news{position:absolute;left:0;top:1140px;width:1200px;height:479px;background:var(--light-bg)}
.news h2{position:absolute;left:129px;top:66px;font-size:27px;font-weight:500;color:var(--green)}
.see-all{position:absolute;left:956px;top:82px;width:108px;height:31px;background:var(--green);color:var(--white);font-size:10px;font-weight:600;display:flex;align-items:center;justify-content:center}
.news-card{position:absolute;top:146px;width:295px;height:259px;background:var(--white);box-shadow:0 1px 3px rgba(0,0,0,.08)}
.news-card .chev{position:absolute;left:24px;top:34px;width:25px;height:25px;border:1px solid #999;display:flex;align-items:center;justify-content:center}
.news-card h3{position:absolute;left:78px;top:26px;width:205px;font-size:15px;font-weight:500;line-height:26px}
.news-card p{position:absolute;left:78px;top:96px;width:198px;font-size:10.5px;line-height:20px;letter-spacing:-.1px;color:var(--grey-text);text-align:justify}
.news-card .btn-s{position:absolute;left:78px;top:196px}

/* feature tiles */
.tile{position:absolute;top:1707px;width:295px;height:326px;display:flex;align-items:flex-end;justify-content:center;padding-bottom:34px;color:var(--white);font-size:22px;font-weight:500;text-align:center;line-height:28px}
.tile-btn{position:absolute;top:2053px}

/* sports */
.sports{position:absolute;left:0;top:2172px;width:1200px;height:428px;background:linear-gradient(100deg,#3f5a6e 0%,#8a9aa6 30%,#c9b9a8 55%,#7e6f76 80%,#3f4b5e 100%)}
.sports h2{position:absolute;left:0;top:140px;width:1200px;text-align:center;color:var(--white);font-size:46px;font-weight:600}
.sports a{position:absolute;left:422px;top:231px;width:356px;height:50px;background:var(--orange);color:var(--white);font-size:16px;font-weight:600;display:flex;align-items:center;justify-content:center;text-decoration:none}

/* footer */
.site-footer{position:absolute;left:0;top:2600px;width:1200px;height:332px;background:var(--dark);border-top:4px solid var(--green);color:#ddd;font-size:11px}
.foot-col{position:absolute;top:54px;list-style:none}
.foot-col li{height:29px}
.foot-brand{position:absolute;left:872px;top:80px;display:flex;align-items:center;gap:10px;font-size:20px;font-weight:700;color:var(--white);letter-spacing:1px}
.foot-brand i{width:12px;height:12px;background:var(--green)}
.foot-rule{position:absolute;left:133px;top:231px;width:938px;height:1px;background:#555}
.copyright{position:absolute;left:0;top:275px;width:1200px;text-align:center;font-size:10px;color:#bbb}
</style>
</head>
<body>
<div class="page">

  <header class="site-header">
    <div class="brand"><span class="brand-dot"></span>BRACKMOOR HALLS</div>
    <div class="tagline">Daleshire's Premier Entertainment &amp; Sporting Centre</div>
    <div class="utility">
      <span><i></i>Gift Voucher</span>
      <span><i></i>Join our Mailing List</span>
      <span><i></i>My Account</span>
      <span><i></i>Basket</span>
      <span><i></i>Register</span>
    </div>
    <div class="box-office">
      <div class="phone-icon">
        <svg width="18" height="18" viewBox="0 0 24 24"><path d="M6.6 10.8a15 15 0 006.6 6.6l2.2-2.2c.3-.3.7-.4 1-.2 1.1.4 2.3.6 3.6.6.6 0 1 .4 1 1V20c0 .6-.4 1-1 1A17 17 0 013 4c0-.6.4-1 1-1h3.5c.6 0 1 .4 1 1 0 1.3.2 2.5.6 3.6.1.3 0 .7-.2 1z" fill="#fff"/></svg>
      </div>
      <div><small>BOX OFFICE</small><strong>01632 960 418</strong></div>
    </div>
    <div class="search">
      <svg width="11" height="11" viewBox="0 0 12 12"><circle cx="5" cy="5" r="3.8" fill="none" stroke="#ccc" stroke-width="1.5"/><path d="M8 8l3 3" stroke="#ccc" stroke-width="1.5"/></svg>
      SEARCH
    </div>
    <div class="follow">Follow us :
      <span class="dot" style="background:#3b5bb0"></span>
      <span class="dot" style="background:#2aa3e0"></span>
      <span class="dot" style="background:#e0612f"></span>
    </div>
  </header>

  <nav class="main-nav">
    <span>What's On</span><span>Conferencing &amp; Events</span><span>Sports &amp; Leisure</span><span>Lantern Theatre</span><span>Plan Your Visit</span><span>News</span><span>Discover More</span><span>Contact Us</span>
  </nav>

  <section class="hero" role="img" aria-label="Photo of a conference hall with chairs in gold covers">
    <div class="hero-copy">
      <h2>WELCOME TO</h2>
      <h1>BRACKMOOR</h1>
      <div class="date">07 <sup style="font-size:9px">TH</sup> OF JANUARY, 2017</div>
      <p>Lorem Ipsum is simply dummy text of the printing and typesetting industry. Lorem Ipsum has been the industry's.</p>
    </div>
    <div class="hero-btn more"><svg width="18" height="18"><path d="M9 1v16M1 9h16" stroke="#fff" stroke-width="2"/></svg>MORE</div>
    <div class="hero-btn book"><svg width="20" height="20" viewBox="0 0 20 20"><path d="M3 17l1-4L14 3l3 3L7 16z" fill="none" stroke="#fff" stroke-width="1.6"/></svg>BOOK</div>
    <div class="dots"><span></span><span class="on"></span><span></span><span></span></div>
  </section>

  <div class="arrow" style="left:42px"><svg width="10" height="14"><path d="M8 1L2 7l6 6" fill="none" stroke="#777" stroke-width="1.5"/></svg></div>
  <div class="arrow" style="left:1112px"><svg width="10" height="14"><path d="M2 1l6 6-6 6" fill="none" stroke="#777" stroke-width="1.5"/></svg></div>

  <article class="event-card" style="left:131px">
    <div class="photo" role="img" aria-label="Photo of a theatre auditorium with tiered seating" style="background:linear-gradient(180deg,#6b3a2e,#b0573a)"></div>
    <h3>Heading 1</h3>
    <div class="when">01 <sup style="font-size:7px">st</sup>&nbsp;of January, 2017</div>
    <div class="mini-btns"><span class="btn-s blue">+ MORE</span><span class="btn-s orange">✎ BOOK</span></div>
  </article>
  <article class="event-card" style="left:367px">
    <div class="photo" role="img" aria-label="Photo of a banqueting hall with round tables" style="background:linear-gradient(180deg,#4a3a3a,#9a8070)"></div>
    <h3>Heading 2</h3>
    <div class="when">07 <sup style="font-size:7px">th</sup>&nbsp;of January, 2017</div>
    <div class="mini-btns"><span class="btn-s blue">+ MORE</span><span class="btn-s orange">✎ BOOK</span></div>
  </article>
  <article class="event-card" style="left:603px">
    <div class="photo" role="img" aria-label="Photo of a meeting room set up boardroom style" style="background:linear-gradient(180deg,#e0d6c4,#b58a4a)"></div>
    <h3>Heading 3</h3>
    <div class="when">15 <sup style="font-size:7px">th</sup>&nbsp;of January, 2017</div>
    <div class="mini-btns"><span class="btn-s blue">+ MORE</span><span class="btn-s orange">✎ BOOK</span></div>
  </article>
  <article class="event-card" style="left:838px">
    <div class="photo" role="img" aria-label="Photo of a conference room with rows of tables" style="background:linear-gradient(180deg,#ddd2be,#b59448)"></div>
    <h3>Heading 4</h3>
    <div class="when">31 <sup style="font-size:7px">st</sup>&nbsp;of January, 2017</div>
    <div class="mini-btns"><span class="btn-s blue">+ MORE</span><span class="btn-s orange">✎ BOOK</span></div>
  </article>

  <section class="news">
    <h2>Latest From Brackmoor</h2>
    <div class="see-all">SEE ALL NEWS</div>
    <article class="news-card" style="left:131px">
      <span class="chev"><svg width="8" height="12"><path d="M2 1l5 5-5 5" fill="none" stroke="#666" stroke-width="1.4"/></svg></span>
      <h3>Lorem Ipsum is simply dummy text</h3>
      <p>There are many variations of passages of Lorem Ipsum available, but the majority have suffered alteration.</p>
      <span class="btn-s blue">+ MORE</span>
    </article>
    <article class="news-card" style="left:452px">
      <span class="chev"><svg width="8" height="12"><path d="M2 1l5 5-5 5" fill="none" stroke="#666" stroke-width="1.4"/></svg></span>
      <h3>It is a long established fact that a reader</h3>
      <p style="text-align:left">Contrary to popular belief, Lorem Ipsum is not simply random text. It has roots in classical Latin texts.</p>
      <span class="btn-s blue">+ MORE</span>
    </article>
    <article class="news-card" style="left:772px">
      <span class="chev"><svg width="8" height="12"><path d="M2 1l5 5-5 5" fill="none" stroke="#666" stroke-width="1.4"/></svg></span>
      <h3>There are many variations of passages</h3>
      <p style="text-align:left">But I must explain to you how all this mistaken idea of denouncing pleasure and praising pain was born.</p>
      <span class="btn-s blue">+ MORE</span>
    </article>
  </section>

  <div class="tile" role="img" aria-label="Photo of a speaker presenting to a conference audience, blue tint" style="left:131px;background:linear-gradient(180deg,#3a5fb0,#23367a)">CONFERENCES &amp;<br>EVENTS</div>
  <div class="tile" role="img" aria-label="Photo of a party crowd with confetti, warm red tint" style="left:452px;background:linear-gradient(180deg,#8a3b2a,#4a2520)">Parties at<br>Brackmoor</div>
  <div class="tile" role="img" aria-label="Photo of hands typing on a laptop, teal tint" style="left:772px;background:linear-gradient(180deg,#4aa897,#2c7f70)">Co-working<br>Hub</div>
  <span class="btn-s blue tile-btn" style="left:240px">+ MORE</span>
  <span class="btn-s orange tile-btn" style="left:560px;width:72px">+ MORE</span>
  <span class="btn-s green tile-btn" style="left:883px">+ MORE</span>

  <section class="sports" role="img" aria-label="Photo of a fitness class stretching in a gym">
    <h2>SPORTS &amp; LEISURE</h2>
    <a>CLICK HERE FOR MORE INFORMATION</a>
  </section>

  <footer class="site-footer">
    <ul class="foot-col" style="left:133px">
      <li>Brackmoor Entertainment Venue</li><li>Heathfield Close</li><li>Ashcombe</li><li>Daleshire</li><li>DX14 7QR</li>
    </ul>
    <ul class="foot-col" style="left:422px">
      <li>What's on</li><li>Conferencing &amp; Events</li><li>Sports &amp; Leisure</li><li>Lantern Theatre</li>
    </ul>
    <ul class="foot-col" style="left:684px">
      <li>Plan Your Visit</li><li>News</li><li>Discover More</li><li>Contact us</li>
    </ul>
    <div class="foot-brand"><i></i>BRACKMOOR HALLS</div>
    <div class="foot-rule"></div>
    <div class="copyright">Copyrights © 2016 All Rights Reserved</div>
  </footer>

</div>
</body>
</html>
```